Email Marketing Campaign Templates

Email drip childcare campaign designed to communicate with parents interested in services. We would like the template(s) to be created so that we can change the content as needed.I will add below collateral that we have used in the past as well as logo.
three to for templates 1.) welcome template 2/ things to bring 3) generic template
Target Market(s)
Parents and Millennials
Industry/Entity Type
Childcare
Colors
85cae6
0493ce
9bcb3c
add136
fefefe
faa54b
cadf82
86cae7
33a6d7
Requirements
Must have
- Photos of staff with children
Nice to have
- Photos

```html
<!DOCTYPE html>
<html lang="en">
<head>
<meta charset="utf-8">
<title>Bloomwell Early Learning Center – Welcome</title>
<link href="https://fonts.googleapis.com/css2?family=Poppins:wght@400;600;700&family=Lato:wght@400;700&display=swap" rel="stylesheet">
<style>
  :root {
    --sky: #85cae6;
    --sky-light: #86cae7;
    --blue: #33a6d7;
    --blue-deep: #0493ce;
    --leaf-light: #cadf82;
    --leaf: #add136;
    --orange: #faa54b;
    --white: #fefefe;
    --ink: #1c1c1c;
    --body: #6f6f6f;
    --footer-bg: #e1e1e1;
    --footer-ink: #3a3a3a;
  }
  * { box-sizing: border-box; margin: 0; padding: 0; }
  html, body { width: 1200px; height: 2203px; overflow: hidden; background: var(--white); }
  .email { position: relative; width: 1200px; height: 2203px; background: var(--white); font-family: "Lato", Arial, sans-serif; }
  .abs { position: absolute; }

  .header { left: 0; top: 0; width: 1200px; height: 440px; }
  .brand {
    left: 380px; top: 200px; width: 490px; text-align: center;
    font-family: "Poppins", Arial, sans-serif; font-weight: 600; color: var(--blue-deep);
    font-size: 44px; line-height: 1.15;
  }
  .brand small { display: block; font-size: 24px; }

  .welcome-title { left: 137px; top: 545px; font-family: "Poppins", Arial, sans-serif; font-weight: 700; font-size: 48px; color: var(--ink); letter-spacing: -0.3px; }
  .welcome-text { left: 137px; top: 620px; width: 860px; font-family: "Poppins", Arial, sans-serif; font-size: 21px; line-height: 43px; color: var(--body); }

  .section-title { font-family: "Poppins", Arial, sans-serif; font-weight: 600; font-size: 35px; color: var(--ink); }
  .parents-title { left: 134px; top: 770px; }
  .parents-text { left: 134px; top: 840px; width: 480px; font-size: 17.5px; line-height: 32px; color: var(--body); }
  .program-list { left: 138px; top: 1030px; list-style: none; }
  .program-list li { font-size: 18px; color: var(--ink); height: 42.5px; display: flex; align-items: center; gap: 12px; }
  .program-list svg { width: 20px; height: 14px; }

  .btn {
    display: flex; align-items: center; justify-content: space-between;
    height: 58px; border-radius: 29px; background: var(--orange); color: var(--white);
    font-size: 20px; padding: 0 34px 0 30px; text-decoration: none;
  }
  .btn svg { width: 20px; height: 14px; }
  .btn-enroll { left: 126px; top: 1210px; width: 385px; }

  .photo-child { left: 671px; top: 777px; width: 529px; height: 513px;
    background: radial-gradient(ellipse at 50% 55%, #7d7f86 0%, #5c5d62 30%, transparent 55%),
                linear-gradient(120deg, #b9a24a 0%, #8a7f46 35%, #6d6550 60%, #9b6a4a 100%); }

  .panel { top: 1363px; height: 441px; }
  .panel-staff { left: 0; width: 598px; background: var(--leaf-light); }
  .panel-environment { left: 598px; width: 602px; background: var(--leaf); }
  .panel-icon { top: 33px; width: 62px; height: 62px; }
  .panel-title { top: 45px; font-weight: 600; }
  .panel-text { top: 141px; font-size: 17.5px; line-height: 32px; color: #111; width: 420px; }
  .panel .btn { top: 322px; width: 385px; }

  .testimonials { left: 0; top: 1804px; width: 1200px; height: 256px; background: var(--sky); text-align: center; }
  .testimonials .section-title { margin-top: 58px; }
  .testimonials p { margin: 18px auto 0; width: 800px; font-size: 18.5px; line-height: 32px; color: #111; }

  .footer { left: 0; top: 2060px; width: 1200px; height: 143px; background: var(--footer-bg); color: var(--footer-ink); font-size: 17.5px; line-height: 33px; }
  .footer-contact { left: 63px; top: 18px; }
  .footer-hours { right: 40px; top: 18px; text-align: right; }
</style>
</head>
<body>
<div class="email">

  <svg class="abs header" viewBox="0 0 1200 440" aria-hidden="true">
    <path d="M0 0 H1200 V385 Q620 480 0 352 Z" fill="var(--sky)"/>
    <circle cx="624" cy="148" r="288" fill="var(--white)"/>
  </svg>
  <div class="abs brand">Bloomwell<small>Early Learning Center</small></div>

  <h1 class="abs welcome-title">Welcome to your child’s happy place</h1>
  <p class="abs welcome-text">We know that your child is so much more than what they know, so we use an educational approach that considers the whole child.</p>

  <h2 class="abs section-title parents-title">Prospective Parents</h2>
  <p class="abs parents-text">Bloomwell Early Learning Center creates the ideal environment for kids to feel safe, loved, and accepted as they try new ideas, develop academic skills and imitate adult roles. We learn through play and believe that play makes it possible for children to learn social skills and develop friendships.</p>

  <ul class="abs program-list">
    <li>Infant Program <svg viewBox="0 0 20 14"><path d="M1 7 H18 M12 1 L18 7 L12 13" fill="none" stroke="var(--blue)" stroke-width="1.6"/></svg></li>
    <li>Toddler Program <svg viewBox="0 0 20 14"><path d="M1 7 H18 M12 1 L18 7 L12 13" fill="none" stroke="var(--blue)" stroke-width="1.6"/></svg></li>
    <li>Pre-School Program <svg viewBox="0 0 20 14"><path d="M1 7 H18 M12 1 L18 7 L12 13" fill="none" stroke="var(--blue)" stroke-width="1.6"/></svg></li>
    <li>Pre-K Program <svg viewBox="0 0 20 14"><path d="M1 7 H18 M12 1 L18 7 L12 13" fill="none" stroke="var(--blue)" stroke-width="1.6"/></svg></li>
  </ul>

  <a class="abs btn btn-enroll" href="#">Enroll in Bloomwell <svg viewBox="0 0 20 14"><path d="M1 7 H18 M12 1 L18 7 L12 13" fill="none" stroke="var(--white)" stroke-width="1.6"/></svg></a>

  <div class="abs photo-child" role="img" aria-label="Photo of a young child in a grey zip-up jacket playing in a colourful classroom"></div>

  <section class="abs panel panel-staff">
    <svg class="abs panel-icon" style="left:84px" viewBox="0 0 62 62" aria-hidden="true">
      <g fill="none" stroke="#1c1c1c" stroke-width="2.4">
        <rect x="2" y="12" width="58" height="42" rx="2"/>
        <rect x="24" y="4" width="6" height="9"/>
        <line x1="8" y1="22" x2="28" y2="22"/><line x1="8" y1="30" x2="28" y2="30"/><line x1="8" y1="38" x2="24" y2="38"/>
        <rect x="33" y="18" width="22" height="30" rx="2"/>
        <circle cx="44" cy="28" r="4.5"/>
        <path d="M37 44 Q44 34 51 44"/>
      </g>
    </svg>
    <h2 class="abs section-title panel-title" style="left:188px">Meet Our Staff</h2>
    <p class="abs panel-text" style="left:79px">Our staff are all certified child educators. Lorem ipsum dolor sit amet, eget et fusce suspendisse, scelerisque a dictum ut justo, varius varius convallis suspendisse vitae ullamcorper, aliquam mollis aliquam lacinia vehicula.</p>
    <a class="abs btn" style="left:72px" href="#">View Staff Bio’s <svg viewBox="0 0 20 14"><path d="M1 7 H18 M12 1 L18 7 L12 13" fill="none" stroke="var(--white)" stroke-width="1.6"/></svg></a>
  </section>

  <section class="abs panel panel-environment">
    <svg class="abs panel-icon" style="left:84px" viewBox="0 0 62 62" aria-hidden="true">
      <g fill="none" stroke="#1c1c1c" stroke-width="2.4">
        <circle cx="31" cy="18" r="13"/>
        <path d="M16 58 V44 Q16 34 31 34 Q46 34 46 44 V58 Z"/>
        <line x1="22" y1="47" x2="40" y2="47"/>
      </g>
    </svg>
    <h2 class="abs section-title panel-title" style="left:151px">Our Environment</h2>
    <p class="abs panel-text" style="left:81px;width:430px">It’s always a beautiful day at Bloomwell! Our open environment fosters autonomy &amp; community. From an early age, children learn by seeing, doing, and helping their friends. Our outdoor environment encourages imaginative group play.</p>
    <a class="abs btn" style="left:75px" href="#">More Information <svg viewBox="0 0 20 14"><path d="M1 7 H18 M12 1 L18 7 L12 13" fill="none" stroke="var(--white)" stroke-width="1.6"/></svg></a>
  </section>

  <section class="abs testimonials">
    <h2 class="section-title">Testimonials</h2>
    <p>“Lorem ipsum dolor sit amet, eget et fusce suspendisse, scelerisque a dictum ut justo, varius varius convallis suspendisse vitae ullamcorper, aliquam mollis aliquam lacinia vehicula.” - Current Parent</p>
  </section>

  <footer class="abs footer">
    <div class="abs footer-contact">555-014-2230<br>82 Maple Grove Avenue<br>Riverton, Ohio 43099</div>
    <div class="abs footer-hours">We can’t wait to meet your family!<br>Monday - Friday :&nbsp; 7:00 am – 6:00 pm</div>
  </footer>

</div>
</body>
</html>
```